zenLoft - nutrition bars - logo and packaging*

zenLoft develops stress-relief nutrition bars powered by deep profiling machine learning technology, offering personalized stress management routine.
We produce 3 flavors of nutrition bars. in each flavor, we produce 6 stress relief formulations (3 for day, 3 for night) in 2 strengths.

We need a rebranding of our logo and packaging.

Target Market(s)

Full description of the target audience and their needs and lifestyle is explained in the attached presentation

Logo Text

zenLoft

Font styles to use
Script

Colors

Designer to choose colors to be used in the design.

Requirements
Must have
• logo
• Packaging
• Full description of the deliveries is explained in the attached presentation
Nice to have
• concept for boxes, website

```html
<!DOCTYPE html>
<html lang="en">
<head>
<meta charset="utf-8">
<title>zenLoft – Quiet Moss packaging</title>
<link href="https://fonts.googleapis.com/css2?family=Montserrat:wght@500;600;700&display=swap" rel="stylesheet">
<style>
  :root {
    --leaf-green: #2f7a28;
    --sun-orange: #ff8200;
    --paper-white: #ffffff;
    --ink-black: #1a1a1a;
  }
  html, body {
    margin: 0;
    padding: 0;
    overflow: hidden;
    background: var(--paper-white);
  }
  .pack {
    position: relative;
    width: 1200px;
    height: 2688px;
    overflow: hidden;
    background: var(--paper-white);
    font-family: "Montserrat", sans-serif;
  }
  .pack-shapes {
    position: absolute;
    inset: 0;
    width: 1200px;
    height: 2688px;
  }
  .brand-name {
    position: absolute;
    left: 0;
    width: 1200px;
    top: 570px;
    margin: 0;
    text-align: center;
    font-size: 200px;
    font-weight: 700;
    line-height: 1;
    color: var(--ink-black);
    letter-spacing: -2px;
  }
  .flavour {
    position: absolute;
    left: 0;
    width: 1200px;
    text-align: center;
    color: var(--paper-white);
    white-space: nowrap;
  }
  .flavour-name {
    top: 2122px;
    margin: 0;
    font-size: 120px;
    font-weight: 600;
    line-height: 1;
  }
  .flavour-rule {
    position: absolute;
    left: 214px;
    width: 776px;
    top: 2246px;
    height: 6px;
    background: var(--paper-white);
  }
  .flavour-tagline {
    top: 2261px;
    margin: 0;
    font-size: 40px;
    font-weight: 600;
    line-height: 1;
    color: var(--sun-orange);
    letter-spacing: 1.5px;
  }
  .flavour-ingredients {
    top: 2322px;
    margin: 0;
    font-size: 62px;
    font-weight: 600;
    line-height: 1;
    letter-spacing: 1px;
  }
  .net-weight {
    position: absolute;
    left: 896px;
    top: 2484px;
    margin: 0;
    font-size: 32px;
    font-weight: 700;
    line-height: 1;
    color: var(--ink-black);
  }
</style>
</head>
<body>
<main class="pack">
  <svg class="pack-shapes" viewBox="0 0 1200 2688" xmlns="http://www.w3.org/2000/svg" aria-hidden="true">
    <rect class="top-band" x="0" y="0" width="1200" height="88" fill="var(--leaf-green)"/>
    <rect class="top-stripe" x="0" y="88" width="1200" height="24" fill="var(--sun-orange)"/>
    <path class="side-wave" d="M0,980 Q40,1540 350,1860 L0,1960 Z" fill="var(--sun-orange)"/>
    <path class="base-wave" d="M1200,640 C1170,1420 720,1800 0,1960 L0,2688 L1200,2688 Z" fill="var(--leaf-green)"/>
  </svg>

  <h1 class="brand-name">zenLoft</h1>

  <h2 class="flavour flavour-name">QUIET MOSS</h2>
  <div class="flavour-rule"></div>
  <p class="flavour flavour-tagline">Gentle Botanicals &amp; Roots</p>
  <p class="flavour flavour-ingredients">BARLEY &amp; CRANBERRY</p>

  <p class="net-weight">35gr</p>
</main>
</body>
</html>
```